Niche Fitness Rebrand : Q7 Peak Conditioning

We're re-branding our fitness business and need to develop a cleaner, more sophisticated, and sleek website for our clients and potential clients to reference. We're looking to have some photo presence on all pages, with clean, crisp sections for easy reading on the web, and on mobile. We love the BVRdal(.com) website, which represents a very similar target market, and one of the same methods that our business represents. We're looking to take this local studio to a more professional level for future expansion, and need it to be sleek and in line with the growing and competitive marketplace for fitness.
Target Market(s)
70/30 women to men, physically active, upper middle class / professional between the ages of 28-42.
Industry/Entity Type
Fitness
Requirements
Must have
- sleek, professional, high-end design, with easy user navigation.
- About Page - with drop down child pages for management and coaches bios
- Classes Page 'The Methods' - with drop down child pages for different class types
- Location / Schedule Page
- Pricing
- Blog
- Private staff only programming login page
Nice to have
- potential to add an online retail shop -- but not currently necessary.
- Industry websites we like:
- www.bvrdal.example
- www.tarnbrookathletics.example

```html
<!DOCTYPE html>
<html lang="en">
<head>
<meta charset="utf-8">
<title>Q7 Peak Conditioning</title>
<link rel="stylesheet" href="https://fonts.googleapis.com/css2?family=Exo+2:wght@400;500;600;700&family=Lora:ital@1&display=swap">
<style>
:root{
  --ink:#1b1b1b;
  --black:#050505;
  --nav:#0d0d0d;
  --accent:#c8773a;
  --accent-dark:#3a2a20;
  --text:#555;
  --light:#fff;
  --footer:#2c3440;
  --footer-bottom:#222831;
  --muted:#aab2bd;
  --star:#e9b500;
}
*{box-sizing:border-box;margin:0;padding:0}
html,body{width:1200px;height:2691px;overflow:hidden}
body{font-family:"Exo 2",sans-serif;color:var(--text);background:#fff;position:relative}
.abs{position:absolute}
.container{position:absolute;left:149px;width:902px}

/* top bar + nav */
.top-bar{top:0;left:0;width:1200px;height:26px;background:var(--black);color:#ddd;font-size:10px}
.top-bar .hours{left:149px;top:7px;display:flex;align-items:center;gap:5px}
.top-bar .hours i{width:9px;height:9px;border-radius:50%;background:#ddd;display:inline-block}
.social{display:flex;gap:16px}
.social span{width:11px;height:11px;border-radius:50%;background:#ddd;display:block}
.top-bar .social{right:149px;top:7px}
.nav{top:26px;left:0;width:1200px;height:58px;background:var(--nav)}
.brand{display:flex;align-items:center;gap:7px;color:#fff;font-weight:600;font-size:15px;line-height:1}
.brand i{width:14px;height:14px;border:2px solid currentColor;display:block}
.nav .brand{left:149px;top:21px}
.menu{right:149px;top:0;display:flex;gap:36px;height:58px;align-items:center;list-style:none}
.menu li{color:#fff;font-weight:700;font-size:11.5px;text-transform:uppercase;position:relative;height:58px;line-height:58px}
.menu li.active{color:var(--accent)}
.menu li.active::before{content:"";position:absolute;top:0;left:-6px;right:-6px;height:3px;background:var(--accent)}

/* hero */
.hero{top:84px;left:0;width:1200px;height:574px;background:linear-gradient(100deg,#2b231d 0%,#6b5845 35%,#b89a79 62%,#d9c3a6 100%)}
.hero-caption{left:612px;top:352px;color:#fff}
.hero-caption h1{font-size:34px;font-weight:700;line-height:1}
.hero-caption p{font-size:21px;line-height:29px;margin-top:10px}
.btn{display:inline-block;background:var(--accent-dark);color:var(--accent);font-weight:700;font-size:15px;text-transform:uppercase;padding:0 29px;line-height:42px;border-radius:3px;margin-top:22px}
.hero-pager{left:549px;top:630px;width:104px;height:28px;background:var(--accent-dark);display:flex;align-items:center;justify-content:center;gap:6px;color:#fff;font-size:13px}
.hero-pager i{width:8px;height:8px;border-radius:50%;border:1px solid #fff;display:block}
.hero-pager i.on{background:#fff}

/* popular classes */
.classes{top:723px;height:210px;display:flex;gap:11px}
.classes-intro{width:167px;background:var(--black);color:#fff;padding:14px 11px}
.classes-intro h3{font-size:15px;font-weight:700;text-transform:uppercase;line-height:20px}
.classes-intro p{font-size:9.5px;font-style:italic;color:#bbb;line-height:13px;margin-top:8px}
.classes-intro .arrows{display:flex;gap:16px;margin-top:16px;justify-content:center}
.classes-intro .arrows span{width:24px;height:22px;border:1px solid #555;color:#888;font-size:11px;text-align:center;line-height:20px}
.class-card{width:234px;position:relative}
.class-card .tag,.class-card .time{position:absolute;left:0;background:var(--black);color:#fff;font-size:9px;font-weight:700;padding:3px 6px;text-transform:uppercase}
.class-card .tag{top:0}
.class-card .time{bottom:0;font-size:10px;text-transform:none}
.c1{background:linear-gradient(#161616,#333)}
.c2{background:radial-gradient(circle at 50% 40%,#6c5140,#1e1a18 75%)}
.c3{background:radial-gradient(circle at 50% 70%,#ffd25a,#f09a1b 40%,#b05a0a 85%)}

/* welcome */
.welcome{top:992px}
.welcome h2,.testimonials h2{font-size:18px;font-weight:600;color:var(--ink);text-transform:uppercase;margin-left:19px}
.welcome p{font-size:13px;line-height:23.5px;margin-top:24px;padding-left:19px}
.welcome a{color:var(--accent);font-weight:600;text-decoration:none}

/* transformation band */
.band{top:1290px;left:0;width:1200px;height:382px;background:linear-gradient(90deg,#0c0a10 0%,#1a1118 45%,#3a1320 70%,#140d14 100%)}
.band-text{left:169px;top:119px;width:590px;color:#fff}
.band-text h2{font-size:18px;font-weight:600;text-transform:uppercase}
.band-text h4{font-size:13px;font-weight:600;color:#ccc;margin-top:10px}
.band-text p{font-size:13px;line-height:23px;margin-top:22px;color:#ddd}
.band-figure{left:760px;top:0;width:300px;height:382px;background:radial-gradient(ellipse at 50% 45%,#6b2630,#2a1018 70%,transparent)}
.band .arrow{top:170px;color:#fff;font-size:30px;line-height:1}
.band .dots{left:580px;top:352px;display:flex;gap:5px}
.dots i{width:8px;height:8px;border-radius:50%;background:#ddd;display:block}
.dots i.on{background:var(--accent)}

/* testimonials */
.testimonials{top:1732px}
.testimonials .sub{font-size:14px;color:#666;margin:6px 0 0 21px}
.avatars{left:509px;top:1801px;width:182px;height:70px}
.avatars span{position:absolute;border-radius:50%;background:#cfcfcf;border:3px solid #fff}
.t-pager{left:560px;top:1887px;display:flex;gap:5px;align-items:center;color:#e0b89a;font-size:11px}
.t-pager i{width:6px;height:6px;border-radius:50%;background:var(--accent);display:block}
.quote{left:330px;top:1910px;width:540px;text-align:center;font-family:"Lora",serif;font-style:italic;font-size:14px;line-height:22.5px;color:#777}
.reviewer{left:330px;top:1989px;width:540px;text-align:center;font-size:12px;color:#333}
.reviewer .sep{margin:0 12px}
.reviewer .stars{color:var(--star);letter-spacing:1px}

/* map + contact card */
.map{top:2072px;left:0;width:1200px;height:284px;background:linear-gradient(135deg,#e4eaf0,#d5dde6)}
.contact-card{left:149px;top:2115px;width:422px;height:174px;background:#fff;border:1px solid #ccc;padding:18px 0 0 28px;font-size:12px;color:#333;line-height:20px}
.contact-card b{font-weight:700}
.contact-card .col2{position:absolute;left:215px;top:18px}
.contact-card .brand{color:#111;font-size:14px}
.ico{display:inline-block;width:12px;color:#333;font-size:10px}

/* footer */
.footer{top:2356px;left:0;width:1200px;height:296px;background:var(--footer);color:var(--muted);font-size:11px}
.footer .brand{left:149px;top:56px;color:#fff}
.footer .about{left:149px;top:112px;width:230px;line-height:17px}
.footer h5{font-size:10px;color:var(--accent);font-weight:700;text-transform:uppercase}
.f-links{left:434px;top:48px}
.f-links ul{list-style:none;margin-top:14px;line-height:23px}
.f-links li.hl{color:#fff;font-weight:600}
.f-office{left:617px;top:48px;color:#fff;line-height:19px}
.f-office p{margin-top:12px}
.f-sub{left:888px;top:48px}
.f-sub .input{width:163px;height:26px;background:#fff;border-radius:3px;margin-top:10px;color:#999;font-size:9px;padding:7px 10px}
.f-sub .send{width:163px;height:26px;background:var(--accent);border-radius:3px;margin-top:6px;color:#fff;font-size:10px;font-weight:700;text-align:center;line-height:26px;text-transform:uppercase}
.f-sub .social{margin:18px 0 0 34px;gap:22px}
.f-sub .social span{background:#fff}
.built{left:942px;top:268px;color:#fff;font-size:10px}
.built b{color:#e0245e}
.to-top{left:1103px;top:2620px;width:42px;height:42px;border-radius:50%;background:var(--accent);color:#fff;font-size:20px;text-align:center;line-height:40px}
.bottom-bar{top:2652px;left:0;width:1200px;height:39px;background:var(--footer-bottom);color:#ccd;font-size:9.5px}
.bottom-bar .copy{left:149px;top:14px}
.bottom-bar .legal{right:149px;top:14px}
</style>
</head>
<body>

<div class="abs top-bar">
  <div class="abs hours"><i></i>Mon - Sat 6:00 am to 9:00 am (EST)</div>
  <div class="abs social"><span></span><span></span><span></span><span></span></div>
</div>

<header class="abs nav">
  <div class="abs brand"><i></i>Q7 Peak Conditioning</div>
  <ul class="abs menu">
    <li class="active">Home</li><li>Instructors</li><li>Buy Classes</li><li>Locations</li><li>About Us</li><li>Contact Us</li>
  </ul>
</header>

<section class="abs hero" role="img" aria-label="Photo of five smiling fitness clients in a sunlit training studio">
  <div class="abs hero-caption" style="top:268px;left:612px">
    <h1>MAKING FITNESS FUN</h1>
    <p>Lorem ipsum dolor sit amet, consecteturadip<br>isicing elit, sed do eiusmod tempor</p>
    <span class="btn">Know More</span>
  </div>
</section>
<div class="abs hero-pager">&larr;<i></i><i class="on"></i><i class="on"></i>&rarr;</div>

<section class="container classes">
  <div class="classes-intro">
    <h3>Popular<br>Classes</h3>
    <p>Lorem ipsum dolor sit amet, consectetur adipisicing elit, sed eiusmod tempor incididunt</p>
    <p>Labore et dolore magna aliqua Ut enim ad minimet dolorem adipisicing ad minim</p>
    <div class="arrows"><span>&lt;</span><span>&gt;</span></div>
  </div>
  <div class="class-card c1" role="img" aria-label="Photo of a woman holding a side plank on a mat"><span class="tag">Body Stretching</span><span class="time">6 am - 7 am</span></div>
  <div class="class-card c2" role="img" aria-label="Photo of a muscular man flexing"><span class="tag">Body Building</span><span class="time">7 am - 8 am</span></div>
  <div class="class-card c3" role="img" aria-label="Photo of a runner silhouetted against a sunset"><span class="tag">Weight Loss</span><span class="time">8 am - 9 am</span></div>
</section>

<section class="container welcome">
  <h2>Welcome to Q7 Peak Conditioning</h2>
  <p>Lorem ipsum dolor sit amet, consectetur adipisicing elit, sed do eiusmod tempor incididunt ut labore et dolore magna aliqua. Ut enim ad minim veniam, quis nostrud exercitation ullamco laboris nisi ut aliquip ex ea commodo consequat. Duis aute irure dolor in reprehenderit in voluptate velit esse cillum dolore eu fugiat nulla pariatur. Excepteur sint occaecat cupidatat non proident, sunt in culpa qui officia deserunt mollit anim id est laborum.</p>
  <p style="margin-top:14px">Sed ut perspiciatis unde omnis iste natus error sit voluptatem accusantium doloremque laudantium, totam rem aperiam, eaque ipsa quae ab illo inventore veritatis et quasi architecto beatae vitae dicta sunt explicabo. Nemo enim ipsam voluptatem quia voluptas sit aspernatur aut odit aut fugit, sed quia consequuntur magni dolores eos qui ratione voluptatem sequi nesciunt.... <a>Continue Reading</a></p>
</section>

<section class="abs band">
  <div class="abs band-figure" role="img" aria-label="Photo of a muscular athlete against a dark red smoky backdrop"></div>
  <div class="abs band-text">
    <h2>Whole Body Transfomation</h2>
    <h4>we help you transform your body, age is not a barier.</h4>
    <p>Lorem ipsum dolor sit amet, consectetur adipisicing elit, sed do eiusmod tempor incididunt ut labore et dolore magna aliqua. Ut enim ad minim veniam, quis nostrud exercitation ullamco laboris nisi ut aliquip exea commodo consequat.</p>
  </div>
  <span class="abs arrow" style="left:22px">&larr;</span>
  <span class="abs arrow" style="right:22px">&rarr;</span>
  <div class="abs dots"><i class="on"></i><i></i><i></i></div>
</section>

<section class="container testimonials">
  <h2 style="margin-left:19px">Testimonials</h2>
  <p class="sub">What clients say about us</p>
</section>
<div class="abs avatars">
  <span role="img" aria-label="Client portrait" style="left:0;top:8px;width:56px;height:56px"></span>
  <span role="img" aria-label="Client portrait" style="right:0;top:8px;width:56px;height:56px"></span>
  <span role="img" aria-label="Featured client portrait" style="left:51px;top:0;width:72px;height:72px;background:#b9a89a"></span>
</div>
<div class="abs t-pager">&larr; <i style="opacity:.5"></i><i></i><i style="opacity:.5"></i> &rarr;</div>
<p class="abs quote">Lorem ipsum dolor sit amet, consectetur adipisicing elit, sed do eiusmod tempor incididunt ut labore et dolore magna aliqua. Ut enim ad minim veniam,laboris nisi ut aliquip ex ea commodo consequat.</p>
<p class="abs reviewer">Lena Marsh<span class="sep">|</span>weight loss class<span class="sep">|</span><span class="stars">★★★★★</span></p>

<section class="abs map" role="img" aria-label="Street map showing the studio location"></section>
<div class="abs contact-card">
  <div><span class="ico">⌂</span><b>Q7 Peak Conditioning LLC</b></div>
  <div style="padding-left:18px">482 W Larkspur Avenue<br>Hollisford, PA 15990</div>
  <div style="margin-top:6px"><span class="ico">☎</span><b>555-014-2270</b></div>
  <div><span class="ico">☎</span><b>555-014-3381</b></div>
  <div><span class="ico">☎</span><b>555-014-4492</b></div>
  <div class="col2">
    <div class="brand"><i></i>Q7 Peak Conditioning</div>
    <div style="margin-top:38px"><span class="ico">✉</span><b>hello@q7peak.example</b></div>
    <div><span class="ico">◷</span>Mon - Sat 09 am - 06 pm</div>
  </div>
</div>

<footer class="abs footer">
  <div class="abs brand"><i></i>Q7 Peak Conditioning</div>
  <p class="abs about">Lorem ipsum dolor sit amet, consectetur adipisicing elit, sed doeius</p>
  <div class="abs f-links">
    <h5>Quick Links</h5>
    <ul><li>Home</li><li>Instructors</li><li class="hl">Buy Classes</li><li>Locations</li><li>About us</li><li>Contact us</li></ul>
  </div>
  <div class="abs f-office">
    <h5>Corporate Office</h5>
    <p><span class="ico" style="color:#fff">⌂</span><b>Q7 Peak Conditioning LLC</b><br><span style="padding-left:16px">482 W Larkspur Avenue</span><br><span style="padding-left:16px">Hollisford, PA 15990</span></p>
    <p><span class="ico" style="color:#fff">☎</span>555-014-TRAIN (8724)</p>
    <p style="margin-top:6px"><span class="ico" style="color:#fff">✉</span>hello@q7peak.example</p>
  </div>
  <div class="abs f-sub">
    <h5>Subscribe</h5>
    <div class="input">enter your email</div>
    <div class="send">➤ Send</div>
    <div class="social"><span></span><span></span><span></span><span></span></div>
  </div>
  <div class="abs built">Built with <b>♥</b> at <strong>USA</strong></div>
</footer>
<div class="abs to-top">↑</div>

<div class="abs bottom-bar">
  <div class="abs copy">Copyright 2015 - 2016 - Q7 Peak Conditioning LLC | Sitemap</div>
  <div class="abs legal">Privacy Policy &nbsp;|&nbsp; Terms &amp; Conditions &nbsp;|&nbsp; Cookie Policy</div>
</div>

</body>
</html>
```